Health Care Company with Logo Needs Business Cards designed

We are a luxury behavioral health company looking for business cards design we already have a logo and are looking for someone to design a sophisticated luxurious looking business card. Please note that Card design should be captivating just like the logo and also encompass the logo color

Industry/Entity Type

Healthcare

Contact Information for Business Card

Logo,company name, tagline, my name and title, contact details, and physical address

```html
<!DOCTYPE html>
<html lang="en">
<head>
<meta charset="utf-8">
<title>Halden Behavioral Health – Business Card</title>
<link href="https://fonts.googleapis.com/css2?family=Montserrat:wght@400;500;600&family=Roboto+Condensed:wght@700&display=swap" rel="stylesheet">
<style>
  :root {
    --stage: #cccccc;
    --card: #ffffff;
    --orange: #f89734;
    --blue: #00aeef;
    --green: #8dc63f;
    --purple: #814c9e;
    --ink: #333333;
    --ink-soft: #3d3d3d;
  }
  * { margin: 0; padding: 0; box-sizing: border-box; }
  html, body {
    width: 1000px;
    height: 1200px;
    overflow: hidden;
    background: var(--stage);
  }
  .sheet {
    position: relative;
    width: 1000px;
    height: 1200px;
  }
  .card {
    position: absolute;
    left: 51px;
    width: 898px;
    height: 538px;
    background: var(--card);
    overflow: hidden;
  }
  .card--front { top: 44px; }
  .card--back { top: 616px; }
  .card__waves {
    position: absolute;
    inset: 0;
    width: 100%;
    height: 100%;
  }
  .wave--orange { fill: var(--orange); }
  .wave--blue { fill: var(--blue); }
  .wave--green { fill: var(--green); }
  .wave--purple { fill: var(--purple); }

  /* Front: brand block */
  .brand-block {
    position: absolute;
    left: 130px;
    top: 146px;
    width: 220px;
  }
  .brand-block__square {
    width: 78px;
    height: 78px;
    background: var(--orange);
    margin-bottom: 16px;
  }
  .brand-block__name {
    font-family: "Roboto Condensed", "Arial Narrow", sans-serif;
    font-weight: 700;
    font-size: 34px;
    line-height: 1.05;
    color: var(--purple);
  }

  /* Front: contact */
  .contact {
    position: absolute;
    left: 541px;
    top: 254px;
    font-family: "Montserrat", Arial, sans-serif;
    color: var(--ink);
  }
  .contact__name {
    font-weight: 600;
    font-size: 24px;
    line-height: 30px;
  }
  .contact__title {
    font-weight: 400;
    font-size: 23px;
    line-height: 30px;
    color: var(--ink-soft);
    margin-bottom: 12px;
  }
  .contact__list { list-style: none; }
  .contact__item {
    display: flex;
    align-items: center;
    height: 36.5px;
    font-size: 21.5px;
    font-weight: 400;
    color: var(--ink-soft);
  }
  .contact__icon {
    width: 22px;
    height: 22px;
    background: var(--orange);
    border-radius: 2px;
    margin-right: 10px;
    flex: none;
  }
  .contact__icon svg { display: block; width: 22px; height: 22px; }

  /* Back: identity */
  .identity {
    position: absolute;
    left: 130px;
    top: 218px;
    display: flex;
    align-items: center;
  }
  .identity__square {
    width: 92px;
    height: 92px;
    background: var(--purple);
    margin-right: 40px;
    flex: none;
  }
  .identity__name {
    font-family: "Roboto Condensed", "Arial Narrow", sans-serif;
    font-weight: 700;
    font-size: 57px;
    line-height: 60px;
    color: var(--purple);
    white-space: nowrap;
  }
  .identity__tagline {
    font-family: "Roboto Condensed", "Arial Narrow", sans-serif;
    font-weight: 700;
    font-size: 16px;
    letter-spacing: 3.6px;
    color: var(--blue);
    margin-top: 6px;
    white-space: nowrap;
  }
</style>
</head>
<body>
<main class="sheet">

  <section class="card card--front" aria-label="Business card front">
    <svg class="card__waves" viewBox="0 0 1062 636" preserveAspectRatio="none" aria-hidden="true">
      <path class="wave--orange" d="M0 0 H1062 V58 C1000 72 960 80 900 76 C700 66 500 20 350 20 C200 20 80 38 0 58 Z"/>
      <path class="wave--blue" d="M0 70 C100 44 220 28 350 26 C520 26 720 78 900 124 C960 136 1010 120 1062 75 V100 C1010 128 950 140 880 130 C700 104 520 44 350 40 C220 38 100 70 0 98 Z"/>
      <path class="wave--green" d="M0 535 C80 512 160 505 240 508 C420 516 600 600 760 606 C880 610 980 575 1062 540 V565 C980 598 880 620 760 618 C600 616 420 550 240 540 C150 535 80 548 0 563 Z"/>
      <path class="wave--purple" d="M0 578 C60 564 140 558 230 560 C420 566 600 612 760 614 C880 616 980 594 1062 578 V636 H0 Z"/>
    </svg>

    <div class="brand-block">
      <div class="brand-block__square"></div>
      <p class="brand-block__name">Halden<br>Behavioral<br>Health</p>
    </div>

    <div class="contact">
      <h1 class="contact__name">Your Name</h1>
      <p class="contact__title">Manager</p>
      <ul class="contact__list">
        <li class="contact__item">
          <span class="contact__icon"><svg viewBox="0 0 22 22" aria-hidden="true"><path d="M7 5 l2.5 0 l1 3.5 l-1.6 1.2 c0.8 1.6 1.8 2.6 3.4 3.4 l1.2 -1.6 l3.5 1 l0 2.5 c-6 0.6 -10.6 -4 -10 -10 z" fill="#fff"/></svg></span>
          123 444 555
        </li>
        <li class="contact__item">
          <span class="contact__icon"><svg viewBox="0 0 22 22" aria-hidden="true"><path d="M11 4 a4 4 0 0 1 4 4 c0 3 -4 7 -4 7 s-4 -4 -4 -7 a4 4 0 0 1 4 -4 z" fill="none" stroke="#fff" stroke-width="1.5"/><circle cx="11" cy="8" r="1.4" fill="#fff"/><path d="M7 17.5 h8" stroke="#fff" stroke-width="1.5"/></svg></span>
          789 Your Street Here
        </li>
        <li class="contact__item">
          <span class="contact__icon"><svg viewBox="0 0 22 22" aria-hidden="true"><rect x="4" y="6.5" width="14" height="9" fill="none" stroke="#fff" stroke-width="1.4"/><path d="M4 6.5 l7 5.5 l7 -5.5 M4 15.5 l5 -4.5 M18 15.5 l-5 -4.5" fill="none" stroke="#fff" stroke-width="1.2"/></svg></span>
          info@yourname.com
        </li>
        <li class="contact__item">
          <span class="contact__icon"><svg viewBox="0 0 22 22" aria-hidden="true"><circle cx="11" cy="11" r="6.5" fill="none" stroke="#fff" stroke-width="1.3"/><ellipse cx="11" cy="11" rx="3" ry="6.5" fill="none" stroke="#fff" stroke-width="1.1"/><path d="M4.5 11 h13 M6 7.5 h10 M6 14.5 h10" stroke="#fff" stroke-width="1.1"/></svg></span>
          www.yourname.com
        </li>
      </ul>
    </div>
  </section>

  <section class="card card--back" aria-label="Business card back">
    <svg class="card__waves" viewBox="0 0 1062 636" preserveAspectRatio="none" aria-hidden="true">
      <path class="wave--orange" d="M0 0 H1062 V58 C1000 40 900 22 760 21 C560 21 360 76 200 76 C120 76 50 68 0 58 Z"/>
      <path class="wave--blue" d="M0 73 C60 90 120 98 200 94 C380 84 560 28 760 26 C880 26 980 48 1062 68 V98 C980 72 880 44 760 45 C560 46 360 120 200 128 C110 132 50 120 0 100 Z"/>
      <path class="wave--green" d="M0 540 C100 575 200 600 320 600 C520 600 720 508 900 508 C960 508 1020 520 1062 535 V565 C1010 548 950 538 880 540 C700 548 520 612 320 612 C200 612 90 590 0 566 Z"/>
      <path class="wave--purple" d="M0 578 C100 600 200 610 320 610 C560 610 760 560 920 558 C980 558 1030 566 1062 578 V636 H0 Z"/>
    </svg>

    <div class="identity">
      <div class="identity__square"></div>
      <div class="identity__text">
        <h2 class="identity__name">Halden Behavioral Health</h2>
        <p class="identity__tagline">DEDICATED TO HOPE, HEALING AND RECOVERY</p>
      </div>
    </div>
  </section>

</main>
</body>
</html>
```